Investment Management Model Portfolio PDF Flyer

Our clients are retirees and soon-to-be retirees looking for help managing their investment portfolio. Our company designed model portfolios that offer more customization options than competitors' model portfolios. We want to show potential clients that we can provide customization (i.e. "tilts") that allow personalization. Clients can opt for portfolios with more dividends, international exposure, socially-responsible ESG choices, and anything inbetween. Unlike competitors our approach is not one-size-fits-all.

The process of building a portfolio lends itself to metaphors or pictures to do with: building a custom portfolio (DIY-friendly), global diversification (accessing global markets instead of just local markets), and environmentally & socially responsible options (clean energy, rain forest)

Target Market(s)

Seniors (age 65+), retired persons, investors

Industry/Entity Type

Financial Planning

Font styles to use
Serif
Other font styles liked:
• Rufina Bold, Rufina

Colors
ec1f27
0356a4

Requirements
Must have
• -Must use color palette in attached PDF
-Must use pie chart / doughnut chart to represent asset allocation
-At least 4 "asset allocations" for basic benchmark (20/80, 40/60, 60/40, 80/20)
-At least 3 "tilts" are described as Dividend, ESG, and International
Nice to have
• -Asset allocations can be named: conservative, conservative growth, moderate, and growth (20/80, 40/60, 60/40, 80/20, respectively)
-Dividend paying, international and ESG could be represented in pictures or graphics (dividends = money returned to client, international could show a globe or try to represent global markets/currency, ESG is often connected to environmental causes but not only)
Should not have
• -Projected rates of returns

```html
<!DOCTYPE html>
<html lang="en">
<head>
<meta charset="utf-8">
<title>Personalize Your Core Mix | Harbor Retirement Planning</title>
<link href="https://fonts.googleapis.com/css2?family=Rufina:wght@400;700&family=Crimson+Pro:wght@400;600&display=swap" rel="stylesheet">
<style>
  :root {
    --backdrop: #d6d6d6;
    --paper: #f7f7f7;
    --ink: #222222;
    --ink-soft: #444444;
    --brand-red: #ec1f27;
    --brand-blue: #0356a4;
    --split-stock: #3f7bc1;
    --split-bond: #e8414b;
    --tilt-blue: #1646a0;
    --tilt-red: #e0161f;
    --tilt-green: #55a62a;
    --tilt-purple: #9a1d8f;
  }
  * { box-sizing: border-box; margin: 0; padding: 0; }
  html, body {
    width: 1200px; height: 900px; overflow: hidden;
    background: var(--backdrop);
  }
  body { font-family: "Crimson Pro", Georgia, serif; color: var(--ink); }

  .flyer {
    position: absolute; left: 280px; top: 30px;
    width: 640px; height: 840px;
    background: var(--paper);
    padding: 36px 46px 30px;
    display: flex; flex-direction: column;
    overflow: hidden;
  }

  .flyer-header { display: flex; justify-content: space-between; align-items: flex-start; }
  .brand { display: flex; align-items: center; gap: 10px; }
  .brand-mark { width: 22px; height: 22px; background: var(--brand-red); }
  .brand-name {
    font-family: "Rufina", Georgia, serif; font-weight: 400;
    font-size: 26px; line-height: 1; letter-spacing: 1px; color: var(--ink);
  }
  .brand-name small { display: block; font-size: 11px; letter-spacing: 1.5px; margin-top: 3px; }
  .contact { text-align: right; font-size: 12px; line-height: 1.35; color: var(--ink-soft); }

  .flyer-title {
    font-family: "Rufina", Georgia, serif; font-weight: 700;
    font-size: 38px; line-height: 1.1;
    margin-top: 16px; padding-bottom: 6px;
    border-bottom: 2px solid var(--ink);
  }

  .section-heading {
    font-family: "Rufina", Georgia, serif; font-weight: 400;
    font-size: 21px; letter-spacing: 0.5px; text-transform: uppercase;
    margin-top: 14px;
  }

  .split-grid {
    display: grid; grid-template-columns: 1fr 1fr;
    row-gap: 8px; column-gap: 20px; margin-top: 8px;
  }
  .split { display: flex; align-items: center; gap: 16px; }
  .donut { display: block; }
  .donut text { fill: #ffffff; font-family: "Crimson Pro", Georgia, serif; text-anchor: middle; dominant-baseline: middle; }
  .split .donut { width: 122px; height: 122px; }
  .split .donut text { font-size: 2.8px; }

  .split-legend .ratio { font-family: "Rufina", Georgia, serif; font-size: 18px; }
  .split-legend ul { list-style: none; display: flex; gap: 14px; margin-top: 4px; }
  .split-legend li { display: flex; align-items: center; gap: 5px; font-family: "Rufina", Georgia, serif; font-size: 15px; }
  .swatch { width: 14px; height: 14px; flex: none; }
  .swatch.stock { background: var(--split-stock); }
  .swatch.bond { background: var(--split-bond); }
  .swatch.blue { background: var(--tilt-blue); }
  .swatch.red { background: var(--tilt-red); }
  .swatch.green { background: var(--tilt-green); }
  .swatch.purple { background: var(--tilt-purple); }

  .tilt-grid {
    display: grid; grid-template-columns: repeat(3, 1fr);
    column-gap: 18px; margin-top: 10px;
  }
  .tilt { display: flex; flex-direction: column; align-items: flex-start; }
  .tilt-name { font-family: "Rufina", Georgia, serif; font-weight: 700; font-size: 17px; }
  .tilt-legend { list-style: none; margin-top: 5px; }
  .tilt-legend li { display: flex; align-items: center; gap: 6px; font-size: 12px; line-height: 1; margin-bottom: 3px; }
  .tilt-legend li:nth-child(2) { padding-left: 8px; }
  .tilt-legend li:nth-child(3) { padding-left: 16px; }
  .tilt-legend li:nth-child(4) { padding-left: 24px; }
  .tilt .donut { width: 128px; height: 128px; margin-top: 8px; align-self: center; }
  .tilt .donut text { font-size: 2.5px; }
  .tilt .donut text.tiny { font-size: 1.7px; }

  .closing-rule { margin-top: auto; border-top: 2px solid var(--ink); }
</style>
</head>
<body>
<main class="flyer">
  <header class="flyer-header">
    <div class="brand">
      <span class="brand-mark"></span>
      <p class="brand-name">HARBOR<small>RETIREMENT PLANNING, INC.</small></p>
    </div>
    <p class="contact">www.harborwealthdesk.com<br>Call Us: 555-014-2290</p>
  </header>

  <h1 class="flyer-title">Personalize Your Core Mix</h1>

  <h2 class="section-heading">1. Start with Stock/Bond Split</h2>
  <section class="split-grid">
    <div class="split">
      <svg class="donut" viewBox="0 0 42 42" role="img" aria-label="20% stocks, 80% bonds">
        <circle cx="21" cy="21" r="15.9155" fill="none" stroke="var(--split-stock)" stroke-width="8" stroke-dasharray="20 80" stroke-dashoffset="25"/>
        <circle cx="21" cy="21" r="15.9155" fill="none" stroke="var(--split-bond)" stroke-width="8" stroke-dasharray="80 20" stroke-dashoffset="5"/>
        <text x="30.35" y="8.13">20%</text><text x="11.65" y="33.87">80%</text>
      </svg>
      <div class="split-legend">
        <p class="ratio">20/80</p>
        <ul><li><span class="swatch stock"></span>Stocks</li><li><span class="swatch bond"></span>Bonds</li></ul>
      </div>
    </div>
    <div class="split">
      <svg class="donut" viewBox="0 0 42 42" role="img" aria-label="60% stocks, 40% bonds">
        <circle cx="21" cy="21" r="15.9155" fill="none" stroke="var(--split-stock)" stroke-width="8" stroke-dasharray="60 40" stroke-dashoffset="25"/>
        <circle cx="21" cy="21" r="15.9155" fill="none" stroke="var(--split-bond)" stroke-width="8" stroke-dasharray="40 60" stroke-dashoffset="-35"/>
        <text x="36.12" y="25.91">60%</text><text x="5.88" y="16.09">40%</text>
      </svg>
      <div class="split-legend">
        <p class="ratio">60/40</p>
        <ul><li><span class="swatch stock"></span>Stocks</li><li><span class="swatch bond"></span>Bonds</li></ul>
      </div>
    </div>
    <div class="split">
      <svg class="donut" viewBox="0 0 42 42" role="img" aria-label="40% stocks, 60% bonds">
        <circle cx="21" cy="21" r="15.9155" fill="none" stroke="var(--split-stock)" stroke-width="8" stroke-dasharray="40 60" stroke-dashoffset="25"/>
        <circle cx="21" cy="21" r="15.9155" fill="none" stroke="var(--split-bond)" stroke-width="8" stroke-dasharray="60 40" stroke-dashoffset="-15"/>
        <text x="36.12" y="16.09">40%</text><text x="5.88" y="25.91">60%</text>
      </svg>
      <div class="split-legend">
        <p class="ratio">40/60</p>
        <ul><li><span class="swatch stock"></span>Stocks</li><li><span class="swatch bond"></span>Bonds</li></ul>
      </div>
    </div>
    <div class="split">
      <svg class="donut" viewBox="0 0 42 42" role="img" aria-label="80% stocks, 20% bonds">
        <circle cx="21" cy="21" r="15.9155" fill="none" stroke="var(--split-stock)" stroke-width="8" stroke-dasharray="80 20" stroke-dashoffset="25"/>
        <circle cx="21" cy="21" r="15.9155" fill="none" stroke="var(--split-bond)" stroke-width="8" stroke-dasharray="20 80" stroke-dashoffset="-55"/>
        <text x="30.35" y="33.87">80%</text><text x="11.65" y="8.13">20%</text>
      </svg>
      <div class="split-legend">
        <p class="ratio">80/20</p>
        <ul><li><span class="swatch stock"></span>Stocks</li><li><span class="swatch bond"></span>Bonds</li></ul>
      </div>
    </div>
  </section>

  <h2 class="section-heading">2. Tilt Your Preferences</h2>
  <section class="tilt-grid">
    <div class="tilt">
      <h3 class="tilt-name">Socially-Responsible</h3>
      <ul class="tilt-legend">
        <li><span class="swatch blue"></span>ESG</li>
        <li><span class="swatch red"></span>Stocks</li>
        <li><span class="swatch green"></span>Government Bonds</li>
        <li><span class="swatch purple"></span>Corporate Bonds</li>
      </ul>
      <svg class="donut" viewBox="0 0 42 42" role="img" aria-label="50% ESG, 20% stocks, 15% government bonds, 15% corporate bonds">
        <circle cx="21" cy="21" r="15.9155" fill="none" stroke="var(--tilt-blue)" stroke-width="8" stroke-dasharray="50 50" stroke-dashoffset="25"/>
        <circle cx="21" cy="21" r="15.9155" fill="none" stroke="var(--tilt-red)" stroke-width="8" stroke-dasharray="20 80" stroke-dashoffset="-25"/>
        <circle cx="21" cy="21" r="15.9155" fill="none" stroke="var(--tilt-green)" stroke-width="8" stroke-dasharray="15 85" stroke-dashoffset="-45"/>
        <circle cx="21" cy="21" r="15.9155" fill="none" stroke="var(--tilt-purple)" stroke-width="8" stroke-dasharray="15 85" stroke-dashoffset="-60"/>
        <text x="36.9" y="21">50%</text><text x="11.65" y="33.87">20%</text>
        <text x="5.29" y="18.52">15%</text><text x="13.78" y="6.83">15%</text>
      </svg>
    </div>
    <div class="tilt">
      <h3 class="tilt-name">Dividend</h3>
      <ul class="tilt-legend">
        <li><span class="swatch blue"></span>Dividend-Payers</li>
        <li><span class="swatch red"></span>Stocks</li>
        <li><span class="swatch green"></span>Government Bonds</li>
        <li><span class="swatch purple"></span>Corporate Bonds</li>
      </ul>
      <svg class="donut" viewBox="0 0 42 42" role="img" aria-label="65% dividend-paying stocks, 25% stocks, 5% government bonds, 5% corporate bonds">
        <circle cx="21" cy="21" r="15.9155" fill="none" stroke="var(--tilt-blue)" stroke-width="8" stroke-dasharray="65 35" stroke-dashoffset="25"/>
        <circle cx="21" cy="21" r="15.9155" fill="none" stroke="var(--tilt-red)" stroke-width="8" stroke-dasharray="25 75" stroke-dashoffset="-40"/>
        <circle cx="21" cy="21" r="15.9155" fill="none" stroke="var(--tilt-green)" stroke-width="8" stroke-dasharray="5 95" stroke-dashoffset="-65"/>
        <circle cx="21" cy="21" r="15.9155" fill="none" stroke="var(--tilt-purple)" stroke-width="8" stroke-dasharray="5 95" stroke-dashoffset="-70"/>
        <text x="35.17" y="28.22">65%</text><text x="5.29" y="18.52">25%</text>
        <text class="tiny" x="13.78" y="6.83">5%</text><text class="tiny" x="18.52" y="5.29">5%</text>
      </svg>
    </div>
    <div class="tilt">
      <h3 class="tilt-name">International</h3>
      <ul class="tilt-legend">
        <li><span class="swatch blue"></span>International Stocks</li>
        <li><span class="swatch red"></span>Domestic Stocks</li>
        <li><span class="swatch green"></span>Government Bonds</li>
        <li><span class="swatch purple"></span>Corporate Bonds</li>
      </ul>
      <svg class="donut" viewBox="0 0 42 42" role="img" aria-label="56% international stocks, 32% domestic stocks, 6% government bonds, 6% corporate bonds">
        <circle cx="21" cy="21" r="15.9155" fill="none" stroke="var(--tilt-blue)" stroke-width="8" stroke-dasharray="56 44" stroke-dashoffset="25"/>
        <circle cx="21" cy="21" r="15.9155" fill="none" stroke="var(--tilt-red)" stroke-width="8" stroke-dasharray="32 68" stroke-dashoffset="-31"/>
        <circle cx="21" cy="21" r="15.9155" fill="none" stroke="var(--tilt-green)" stroke-width="8" stroke-dasharray="6 94" stroke-dashoffset="-63"/>
        <circle cx="21" cy="21" r="15.9155" fill="none" stroke="var(--tilt-purple)" stroke-width="8" stroke-dasharray="6 94" stroke-dashoffset="-69"/>
        <text x="36.62" y="23.98">56%</text><text x="5.38" y="23.98">32%</text>
        <text class="tiny" x="12.48" y="7.58">6%</text><text class="tiny" x="18.03" y="5.39">6%</text>
      </svg>
    </div>
  </section>

  <div class="closing-rule"></div>
</main>
</body>
</html>
```